Radiant Harbor Holdings business card

We are a real estate advisory and investment company. We are specialized in assisting high networth individuals to invest in real estate overseas. We deliver a very personalized service, anticipating all the potential challenges an investor can face, and making it easy and safe for them. We also co-invest with our clients, assuring them that each project will be looked after as it is our own, and at the same time giving them the extra booth on confidence to invest.

We need a business card design. The business card must have a very premium, high-end look, reflecting principles like "commitment", "trust" and "timeless (but contemporary)". We look for long term relationships with our clients, and we grow with their referrals. We are all about conquering the confidence of the clients by always delivering above the expectations performance.

Target Market(s)

High net worth individuals.

Industry/Entity Type

Real Estate

Contact Information for Business Card

Please consider places on the business card for:

Name
Function (bellow name in smaller size text)

Mobile phone
E-mail
Skype ID
WeChat ID

Adress (3 lines)

Also include the following locations references:
PORTUGAL * DUBAI * HONG KONG

Website: www.rhholdings.example

Requirements
Must have
• Company Logo

```html
<!DOCTYPE html>
<html lang="en">
<head>
<meta charset="utf-8">
<title>Radiant Harbor Holdings – Business Card</title>
<link rel="stylesheet" href="https://fonts.googleapis.com/css2?family=Source+Sans+3:wght@400;600&display=swap">
<style>
  :root {
    --backdrop: #3a3533;
    --card-dark: #0d0d0d;
    --card-blue: #29a9e1;
    --accent-blue: #2ea7e0;
    --text-light: #f2f2f2;
    --text-muted: #9a9a9a;
    --divider: #3a3a3a;
  }
  * { margin: 0; padding: 0; box-sizing: border-box; }
  html, body { width: 1200px; height: 900px; overflow: hidden; }
  body {
    background: var(--backdrop);
    font-family: "Source Sans 3", "Helvetica Neue", Arial, sans-serif;
    position: relative;
  }
  .card {
    position: absolute;
    top: 300px;
    width: 525px;
    height: 300px;
    border-radius: 3px;
    box-shadow: 0 10px 30px rgba(0,0,0,.45);
  }
  /* Front: contact side */
  .card-front { left: 50px; background: var(--card-dark); color: var(--text-light); }
  .front-brand {
    position: absolute; left: 40px; top: 58px;
    display: flex; align-items: center; gap: 10px;
  }
  .brand-dot { width: 12px; height: 12px; border-radius: 50%; background: var(--accent-blue); }
  .front-brand .brand-name {
    font-size: 26px; font-weight: 600; color: var(--accent-blue); letter-spacing: .5px;
  }
  .person { position: absolute; left: 40px; top: 150px; }
  .person-name { font-size: 20px; font-weight: 600; color: var(--accent-blue); }
  .person-role { font-size: 15px; color: var(--text-light); margin-top: 2px; }
  .column-divider {
    position: absolute; left: 262px; top: 128px; width: 1px; height: 90px; background: var(--divider);
  }
  .contacts { position: absolute; left: 282px; top: 124px; list-style: none; }
  .contacts li {
    display: flex; align-items: center; gap: 9px;
    font-size: 15px; line-height: 23px; color: var(--text-light);
  }
  .contacts svg { width: 12px; height: 12px; flex: none; }
  .address { position: absolute; left: 40px; bottom: 34px; font-size: 15px; color: var(--text-light); }
  /* Back: brand side */
  .card-back {
    left: 625px; background: var(--card-blue); color: #fff;
    display: flex; flex-direction: column; align-items: center; justify-content: center;
  }
  .back-brand { display: flex; align-items: center; gap: 10px; }
  .back-brand .brand-dot { background: #fff; }
  .back-brand .brand-name { font-size: 30px; font-weight: 600; letter-spacing: .5px; }
  .locations { margin-top: 26px; font-size: 14px; letter-spacing: .5px; }
  .locations span + span::before { content: "•"; margin: 0 8px; }
  .website { margin-top: 8px; font-size: 13px; }
</style>
</head>
<body>
  <section class="card card-front" aria-label="Business card front">
    <div class="front-brand">
      <span class="brand-dot"></span>
      <span class="brand-name">Radiant Harbor Holdings</span>
    </div>
    <div class="person">
      <p class="person-name">Marcus Ellery</p>
      <p class="person-role">Managing Director</p>
    </div>
    <div class="column-divider"></div>
    <ul class="contacts">
      <li>
        <svg viewBox="0 0 12 12" aria-hidden="true"><rect x="3" y="0.5" width="6" height="11" rx="1" fill="none" stroke="var(--accent-blue)" stroke-width="1.2"/><circle cx="6" cy="9.5" r=".7" fill="var(--accent-blue)"/></svg>
        044-555 010 203
      </li>
      <li>
        <svg viewBox="0 0 12 12" aria-hidden="true"><rect x="0.5" y="2.5" width="11" height="7" fill="var(--accent-blue)"/><path d="M0.5 2.5 6 6.5 11.5 2.5" fill="none" stroke="var(--card-dark)" stroke-width="1"/></svg>
        info@rhholdings.example
      </li>
      <li>
        <svg viewBox="0 0 12 12" aria-hidden="true"><rect x="1" y="1" width="10" height="10" fill="var(--accent-blue)"/></svg>
        /rhholdings.example
      </li>
      <li>
        <svg viewBox="0 0 12 12" aria-hidden="true"><circle cx="6" cy="6" r="5.5" fill="var(--accent-blue)"/></svg>
        /rhholdings.example
      </li>
    </ul>
    <p class="address">12345, Address Goes Here Country Name, 123456.</p>
  </section>

  <section class="card card-back" aria-label="Business card back">
    <div class="back-brand">
      <span class="brand-dot"></span>
      <span class="brand-name">Radiant Harbor Holdings</span>
    </div>
    <p class="locations"><span>PORTUGAL</span><span>DUBAI</span><span>HONG KONG</span></p>
    <p class="website">www.rhholdings.example</p>
  </section>
</body>
</html>
```